Soy Candle Business needs a label design

We need a label design for a new company selling soy candles - Velvet Hearth Co.

We are using apothecary jars in 3 sizes.
As per attached candles will be dressed with a beautiful black bow and all finished with a diamante in centre of bow.

We would like label done on lid of candle jars - 5cm circle (5cm from one side to the other), this way one label will fit each product size. Label will be done as a sticker.

We are thinking of the background colour to be black, however are open to recommendations. We want label to be classy, elegant and simple.

Inspiration for candle design came from attached invitation that features the bow, and beautiful vintage paper on top area.

Label should include the following 3 pieces of information:
Velvet Hearth Co (company name)
Coconut Lime (this will change depending on fragrance)
Soy Candle

Velvet Hearth Co does not have a company logo... what is done for the label will set tone for what is done across other elements of business moving forward.

Industry/Entity Type

Business

Requirements
Must have
• Velvet Hearth Co
Fragrance Flavour
Soy Candle

```html
<!DOCTYPE html>
<html lang="en">
<head>
<meta charset="utf-8">
<title>Velvet Hearth Co — Soy Candle Lid Labels</title>
<link href="https://fonts.googleapis.com/css2?family=Pacifico&family=Josefin+Sans:wght@300;400&display=swap" rel="stylesheet">
<style>
  :root {
    --bg-centre: #ffffff;
    --bg-edge: #d6d6d6;
    --label-black: #0b0b0b;
    --line-white: #ffffff;
    --tint-peach: #f2c7b4;
    --tint-lime: #d3dc2a;
    --tint-sky: #1aa6e0;
    --tint-berry: #a3155f;
  }
  html, body {
    margin: 0;
    padding: 0;
    width: 1200px;
    height: 927px;
    overflow: hidden;
  }
  body {
    background: radial-gradient(ellipse at 50% 45%, var(--bg-centre) 0%, var(--bg-centre) 35%, var(--bg-edge) 100%);
  }
  .label-sheet {
    display: block;
    width: 1200px;
    height: 927px;
  }
  .label--peach { --tint: var(--tint-peach); }
  .label--lime  { --tint: var(--tint-lime); }
  .label--sky   { --tint: var(--tint-sky); }
  .label--berry { --tint: var(--tint-berry); }

  .label__disc { fill: var(--label-black); }
  .label__rim { fill: none; stroke: var(--line-white); stroke-width: 1.4; }
  .label__pattern { fill: var(--tint); opacity: 0.75; }
  .label__stitch { fill: none; stroke: var(--line-white); stroke-width: 1; stroke-dasharray: 3 3; }
  .label__ribbon { fill: var(--tint); stroke: var(--label-black); stroke-width: 1.5; }
  .label__ribbon-stitch { fill: none; stroke: rgba(0,0,0,0.45); stroke-width: 1; stroke-dasharray: 3 3; }
  .label__bow { fill: var(--label-black); stroke: var(--line-white); stroke-width: 1; }
  .label__fragrance {
    font-family: 'Pacifico', cursive;
    font-size: 31px;
    fill: var(--label-black);
  }
  .label__arc-text {
    font-family: 'Josefin Sans', sans-serif;
    font-weight: 300;
    font-size: 14px;
    letter-spacing: 0.5px;
    fill: var(--line-white);
  }
</style>
</head>
<body>
<svg class="label-sheet" viewBox="0 0 1200 927" xmlns="http://www.w3.org/2000/svg">
  <defs>
    <path id="arc-top" d="M -76 0 A 76 76 0 0 1 76 0"/>
    <path id="arc-bottom" d="M -86 0 A 86 86 0 0 0 86 0"/>
    <g id="candle-label">
      <circle class="label__disc" r="106"/>
      <circle class="label__rim" r="101"/>
      <path class="label__pattern" role="img" aria-label="Vintage zigzag paper pattern band"
            fill-rule="evenodd"
            d="M 0 -97 A 97 97 0 1 1 0 97 A 97 97 0 1 1 0 -97 Z M 0 -90 A 90 90 0 1 0 0 90 A 90 90 0 1 0 0 -90 Z"/>
      <path class="label__pattern" role="img" aria-label="Vintage zigzag paper pattern inner band"
            fill-rule="evenodd"
            d="M 0 -66 A 66 66 0 1 1 0 66 A 66 66 0 1 1 0 -66 Z M 0 -56 A 56 56 0 1 0 0 56 A 56 56 0 1 0 0 -56 Z"/>
      <circle class="label__stitch" r="52"/>
      <polygon class="label__ribbon" points="-108,-20 108,-20 100,0 108,20 -108,20 -100,0"/>
      <line class="label__ribbon-stitch" x1="-96" y1="-15" x2="96" y2="-15"/>
      <line class="label__ribbon-stitch" x1="-96" y1="15" x2="96" y2="15"/>
      <rect class="label__bow" role="img" aria-label="Black bow with diamante" x="-13" y="-40" width="26" height="16" rx="5"/>
      <text class="label__fragrance" x="0" y="12" text-anchor="middle">Coconut Lime</text>
      <text class="label__arc-text"><textPath href="#arc-top" startOffset="44%" text-anchor="middle">Velvet Hearth Co</textPath></text>
      <text class="label__arc-text" dy="4"><textPath href="#arc-bottom" startOffset="50%" text-anchor="middle">soy candle</textPath></text>
    </g>
  </defs>

  <use class="label--peach" href="#candle-label" x="215" y="412"/>
  <use class="label--lime"  href="#candle-label" x="465" y="412"/>
  <use class="label--sky"   href="#candle-label" x="712" y="412"/>
  <use class="label--berry" href="#candle-label" x="962" y="412"/>
</svg>
</body>
</html>
```